Tidewell Provisions

Distributor of seasonings and spices to the restaurant industry.

Restaurant

Tidewell Provis
Dean Holcroft
TK Wandsley Distributor
317-640-8917
dean@tidewellprovisionsco.com

No minimum order
Gluten & MSG free soup bases

```html
<!DOCTYPE html>
<html lang="en">
<head>
<meta charset="utf-8">
<title>Tidewell Provisions – Business Card</title>
<link rel="stylesheet" href="https://fonts.googleapis.com/css2?family=PT+Sans:wght@400;700&display=swap">
<style>
  :root {
    --backdrop: #7a5238;
    --card: #ffffff;
    --brand-red: #a51d2d;
    --brand-green: #3f9a3f;
    --ink: #222222;
    --card-shadow: rgba(0, 0, 0, 0.35);
  }
  * { margin: 0; padding: 0; box-sizing: border-box; }
  html, body {
    width: 1200px;
    height: 1000px;
    overflow: hidden;
  }
  body {
    position: relative;
    background: var(--backdrop);
    font-family: "PT Sans", Arial, sans-serif;
    color: var(--ink);
  }
  .card {
    position: absolute;
    left: 265px;
    width: 665px;
    height: 397px;
    background: var(--card);
    border-radius: 28px;
    box-shadow: 0 4px 12px var(--card-shadow);
  }
  .card--front { top: 73px; }
  .card--back { top: 533px; }

  .wordmark {
    position: absolute;
    display: flex;
    align-items: center;
    gap: 12px;
    color: var(--brand-red);
    font-weight: 700;
    white-space: nowrap;
  }
  .wordmark__dot {
    flex: none;
    border-radius: 50%;
    background: var(--brand-red);
  }
  .card--front .wordmark {
    left: 34px;
    top: 172px;
    font-size: 37px;
  }
  .card--front .wordmark__dot { width: 26px; height: 26px; }
  .card--back .wordmark {
    left: 0;
    right: 0;
    justify-content: center;
    top: 168px;
    font-size: 54px;
  }
  .card--back .wordmark__dot { width: 36px; height: 36px; }

  .contact {
    position: absolute;
    left: 373px;
    top: 113px;
  }
  .contact__name {
    color: var(--brand-red);
    font-weight: 700;
    font-size: 20px;
    letter-spacing: 0.3px;
    text-transform: uppercase;
    line-height: 24px;
  }
  .contact__role {
    font-size: 16px;
    line-height: 22px;
  }
  .contact__list {
    list-style: none;
    margin-top: 15px;
    font-size: 16px;
  }
  .contact__list li {
    display: flex;
    align-items: center;
    gap: 7px;
    line-height: 24px;
  }
  .contact__icon {
    width: 14px;
    height: 12px;
    flex: none;
  }
  .features {
    list-style: none;
    margin-top: 8px;
    font-size: 16px;
  }
  .features li {
    display: flex;
    align-items: center;
    gap: 11px;
    line-height: 24px;
  }
  .features li::before {
    content: "";
    width: 7px;
    height: 7px;
    border-radius: 50%;
    background: var(--brand-red);
    flex: none;
    margin-left: 3px;
  }
</style>
</head>
<body>
  <section class="card card--front">
    <div class="wordmark">
      <span class="wordmark__dot"></span>
      <span class="wordmark__name">Tidewell Provis</span>
    </div>
    <div class="contact">
      <p class="contact__name">Dean Holcroft</p>
      <p class="contact__role">TK Wandsley Distributor</p>
      <ul class="contact__list">
        <li>
          <svg class="contact__icon" viewBox="0 0 14 12" aria-hidden="true">
            <path d="M1 4 Q7 -1 13 4 L11 5.5 L9.5 4 Q7 3 4.5 4 L3 5.5 Z" fill="#a51d2d"/>
            <rect x="3" y="6" width="8" height="5" rx="1" fill="#a51d2d"/>
          </svg>
          <span>317-640-8917</span>
        </li>
        <li>
          <svg class="contact__icon" viewBox="0 0 14 12" aria-hidden="true">
            <rect x="1" y="2" width="12" height="8.5" fill="#a51d2d"/>
            <path d="M1.5 2.5 L7 7 L12.5 2.5" fill="none" stroke="#fff" stroke-width="1.2"/>
          </svg>
          <span>dean@tidewellprovisionsco.com</span>
        </li>
      </ul>
      <ul class="features">
        <li>No minimum order</li>
        <li>Gluten &amp; MSG free soup bases</li>
      </ul>
    </div>
  </section>

  <section class="card card--back">
    <div class="wordmark">
      <span class="wordmark__dot"></span>
      <span class="wordmark__name">Tidewell Provis</span>
    </div>
  </section>
</body>
</html>
```